Client case study PDF template design

We have a case study in a word document that we wish to be designed into a visually appealing PDF. This is to be done in Photoshop so that we can re-use it for a number of different case studies.

The design needs to be in keeping with the style of our new website:

http://brightpath.samplework.co.uk/

We are looking for nice data visualisation like seen on infographics. An example of a case study design we like can be seen here:

http://m418305.q47.hv2.filevault.example/wp-content/uploads/2011/08/Ledger-Service-Partner-Showcase1.pdf

The word document can be fetched from here:

https://www.sharebin.example/sh/qwo7tpex2hbrmvk/K8rafPLoXN

Hi Guys,

I have attached a folder with a few images in to the project. I don't know if many of them will be print quality but please take a look and see if there is anything you can use.

Thanks,
Neil

Hi Guys,

Just to be clear, we are not looking for the word document to be copied into a photoshop file. We are looking for a completely new design, only use the word document for the content not a design lead.

Thanks,
Neil

Hi Everyone,

I have to apologise for my lack of contact. I personally hate uncommunicative clients and I am afraid that is exactly what I have been with this project! I got far too busy with the number of projects I have been running and lost sight on a couple, this one included. 

I will be providing feedback today to the designers that we feel have produced the designs closest to what we are looking for. If you don't get feedback today I am afraid that your design didn't quite make it. 

Thanks you for everyones hard work, we are very happy with the quality of designs that have come in. 

Many Thanks,
Neil Hartley

• Nice graphical visualisation of data and a style in-keeping with new website.

```html
<!DOCTYPE html>
<html lang="en">
<head>
<meta charset="utf-8">
<title>BrightPath Case Study – Harlow's Textiles</title>
<link href="https://fonts.googleapis.com/css2?family=Arimo:wght@400;700&family=Oswald:wght@400;500&display=swap" rel="stylesheet">
<style>
  :root {
    --page-bg: #e6e6e7;
    --band: #cfd0d1;
    --paper: #ffffff;
    --green: #6b9a4c;
    --lime: #9cc03f;
    --grey-1: #a9aaac;
    --grey-2: #8d8e90;
    --grey-3: #b1b2b4;
    --grey-4: #949597;
    --grey-light: #d3d4d5;
    --ink: #1e1e1e;
    --white: #ffffff;
  }
  * { margin: 0; padding: 0; box-sizing: border-box; }
  html, body { width: 939px; height: 1200px; overflow: hidden; }
  body {
    position: relative;
    background: var(--page-bg);
    font-family: "Arimo", Arial, sans-serif;
    color: var(--ink);
  }
  .page {
    position: absolute; left: 30px; top: 30px; width: 881px; height: 1140px;
    background: var(--paper);
  }
  .band { position: absolute; left: 30px; width: 881px; background: var(--band); }
  .band--top { top: 30px; height: 36px; }
  .band--bottom { top: 1139px; height: 31px; }

  .section-label {
    position: absolute; left: 30px; width: 193px;
    background: var(--green); color: var(--white);
    font-family: "Oswald", "Arial Narrow", sans-serif; font-weight: 500;
    font-size: 36px; line-height: 1; letter-spacing: 0.5px;
    padding: 0 0 14px 12px;
    display: flex; align-items: flex-end;
  }
  .section-label--challenges { top: 99px; height: 292px; }
  .section-label--solution { top: 438px; height: 418px; flex-direction: column; justify-content: flex-end; align-items: flex-start; }
  .section-label--effects { top: 901px; height: 203px; }

  .row {
    position: absolute; left: 243px; color: var(--white);
    font-size: 15.5px; line-height: 1.18;
    padding: 8px 20px 0 29px;
  }
  .challenge { width: 668px; }
  .challenge--1 { top: 99px; height: 67px; background: var(--grey-1); }
  .challenge--2 { top: 168px; height: 72px; background: var(--grey-2); }
  .challenge--3 { top: 243px; height: 71px; background: var(--grey-3); }
  .challenge--4 { top: 316px; height: 75px; background: var(--grey-4); }

  .solution-intro, .solution-outro {
    position: absolute; left: 273px; width: 610px;
    font-size: 15.5px; line-height: 1.2;
  }
  .solution-intro { top: 437px; }
  .solution-outro { top: 811px; }

  .stat { position: absolute; left: 273px; height: 47px; display: flex; align-items: center; }
  .stat__value {
    width: 94px; height: 47px; background: var(--lime); color: var(--white);
    font-family: "Oswald", "Arial Narrow", sans-serif; font-size: 27px;
    display: flex; align-items: center; justify-content: center;
  }
  .stat__label { margin-left: 12px; font-size: 15.5px; line-height: 1.2; width: 420px; }
  .stat--keywords { top: 498px; }
  .stat--negatives { top: 565px; }
  .stat--campaigns { top: 631px; }
  .stat--adgroups { top: 692px; }
  .stat--adtexts { top: 757px; }

  .effect { width: 449px; }
  .effect--1 { top: 901px; height: 67px; background: var(--grey-3); padding-top: 6px; }
  .effect--2 { top: 970px; height: 67px; background: var(--grey-2); }
  .effect--3 { top: 1039px; height: 65px; background: var(--grey-1); padding-top: 18px; }
  .effect-summary {
    position: absolute; left: 696px; top: 901px; width: 215px; height: 203px;
    background: var(--grey-light); color: var(--white);
    font-size: 15.5px; line-height: 1.2; text-align: center;
    display: flex; align-items: center; justify-content: center; padding: 0 22px 18px;
  }
  strong { font-weight: 700; }
</style>
</head>
<body>
  <div class="page"></div>
  <div class="band band--top"></div>
  <div class="band band--bottom"></div>

  <h2 class="section-label section-label--challenges">CHALLENGES</h2>
  <p class="row challenge challenge--1">Although meant to be representative of the inventory that Harlow's Textiles offered, the reliance on technology had meant that the campaign we not as expansive as it could be.</p>
  <p class="row challenge challenge--2">The market in which Harlow's operates is competitive with low margins. The campaign had struggled to hit the ROI targets and was restricted in what it could spend.</p>
  <p class="row challenge challenge--3">The maintenance of the campaign had been left to the technology solution rather than running with alongside human intervention. As such the structure and targeting of the account was poor.</p>
  <p class="row challenge challenge--4">Harlow's were bought into the use of technology on the account; as such we had to maintain an open mind when evaluating its role in the campaign in the future both in terms of build and management of the campaign.</p>

  <h2 class="section-label section-label--solution"><span>OUR</span><span>SOLUTION</span></h2>
  <p class="solution-intro">BrightPath quickly established that the campaign build could be achieved with more quality and accuracy being built manually than any piece of technology on the market. Number of different solutions trailed.</p>
  <div class="stat stat--keywords"><span class="stat__value">2208%</span><span class="stat__label">BrightPath as a result of a review of the inventory increased keywords within the account</span></div>
  <div class="stat stat--negatives"><span class="stat__value">491%</span><span class="stat__label">Grew the negative keyword list</span></div>
  <div class="stat stat--campaigns"><span class="stat__value">270%</span><span class="stat__label">BrightPath increase the number of campaign</span></div>
  <div class="stat stat--adgroups"><span class="stat__value">8000%</span><span class="stat__label">BrightPath also increased the number of ad groups over</span></div>
  <div class="stat stat--adtexts"><span class="stat__value">1896%</span><span class="stat__label">BrightPath increased the number of unique adtexts</span></div>
  <p class="solution-outro">Over 99.9% of these being completely unique in comparison to previously where 80 – 90% were built using standard templates.</p>

  <h2 class="section-label section-label--effects">EFFECTS</h2>
  <p class="row effect effect--1">A <strong>10%</strong> decrease in the cost per sale, resulting in a higher return on investment throughout the entire campaign.</p>
  <p class="row effect effect--2">Quality Scores improved significantly across the account</p>
  <p class="row effect effect--3">Conversion rates increased <strong>20%</strong> across the board</p>
  <p class="effect-summary">Spend increased by over 100% while delivering a decrease in the cost of sales</p>
</body>
</html>
```